Tom & Nia's Homepage Design - Florists

Hello ArtHivePro,

We’re Tom and Nia and we own a lovely flower shop in Marlow. We’re looking to launch a website that gives our customers all information they need to know about getting in contact with us. In time we hope the website will grow and we will want to add new pages as we go along including ecommerce functionality, so the design will need to allow for this.

The brief:
We are looking for 1 homepage design. We have already had our logo designed, which we’ve attached for you to use. At the moment we’re keen to have a homepage design that showcases six of our most popular bouquets, see attached pictures and our contact details. We are looking for a contemporary design that’s inline with our logo. Please do not use dark background colours, we want a clean, light and simple design that looks fresh, modern and professional. Please remember that the majority of web monitors now use a screen resolution of 1366x768. Therefore please do not design a 800 x 600 homepage.

1. Our logo and icon (See attachments)
2. Potential hero images attached for inspiration. 6 Bouquets attached but dont make it look like a bog standard ecommerce site. You dont have to use the 6 bouquets. Our site is more brand as we dont have ecom functionality yet.
3. Our contact details including:

Name:
Tom and Nia’s (note 1 ‘L’ in Nia’s name, use the logo)

Navigation

Homepage needs to include the following copy
‘Free delivery with all orders”
‘Fresh – 7 days of flower freshness guaranteed’
‘Hand delivered and hand prepared by a professional florist’
Very clear call to action to ‘Order today: 0203 574 2261 or email us (visually a clickable link) today

Payment visuals: show that we accept KORVA/Paymoriant/Harbour Quickcard/Zentrip, with logos

Telephone numbers:
0203 574 2261 (Central London)
0208 417 5309 (Greater London)
01628 735142 (Marlow)
07812 906218 (Mobile)

E-mail address
orders@tomandnias.co.uk (Orders)
CS@tomandnias.co.uk (Customer Service)

Chatterly page link (use CH logo)
http://www.facebook.com/tomandnias

The Northfield Petal Guild logo
Attached should be displayed on the bottom of the homepage somewhere, prefer bottom right.

Other sites we like:
http://www.bloomsbygwendra.com
http://maisonvertilune.com
Like the fun of this one - http://www.puddlegoose.co.uk/goto/home

Our logo should be a good guide for how we’d like the overall page to look, please use this as a starter for your designs. Fee; free to submit your designs and I’ll feedback on changes.

We look forward to seeing your designs!

Tom & Nia

Industry/Entity Type

Florist

Requirements
Must have
• Please see the attached brief. Please use our logo and icon in the design.
Should not have
• Do not use dark background colours, it should feel light and fresh.

```html
<!DOCTYPE html>
<html lang="en">
<head>
<meta charset="utf-8">
<title>Tom &amp; Nia's — Florists</title>
<link rel="stylesheet" href="https://fonts.googleapis.com/css2?family=Ubuntu:wght@300;400;500;700&family=Playfair+Display:ital,wght@1,700&display=swap">
<style>
:root{
  --coral:#ef6461;
  --page:#f6f6f6;
  --white:#ffffff;
  --text:#6d6d6d;
  --muted:#8a8a8a;
  --purple:#8e4aa4;
  --dark:#444444;
  --line:#e6e6e6;
}
*{box-sizing:border-box;margin:0;padding:0}
html,body{width:1073px;height:1200px;overflow:hidden}
body{position:relative;background:var(--coral);font-family:"Ubuntu",sans-serif;color:var(--text)}
.side{position:absolute;top:0;width:124px;height:1200px;background:linear-gradient(180deg,var(--coral),#f0716d 50%,var(--coral))}
.side--left{left:0}.side--right{right:0}
.page{position:absolute;left:124px;top:0;width:826px;height:1200px;background:var(--page)}
.abs{position:absolute}
.brand{left:51px;top:64px;font-size:30px;font-weight:500;color:var(--dark);letter-spacing:-.5px;white-space:nowrap}
.nav{left:392px;top:58px;display:flex;height:55px;align-items:center;font-size:14px;font-weight:300;color:var(--dark)}
.nav a{color:inherit;text-decoration:none;display:block;line-height:55px;white-space:nowrap}
.nav .home{background:var(--coral);color:var(--white);width:74px;text-align:center}
.nav .about{margin-left:21px}.nav .flowers{margin-left:47px}.nav .contact{margin-left:39px}
.hero{left:50px;top:141px;width:725px;height:335px;background:var(--white);border:1px solid var(--line)}
.hero-photo{position:absolute;left:8px;top:8px;width:709px;height:319px;background:linear-gradient(170deg,#ecedea 0%,#e3e6df 35%,#9fb48a 55%,#5e7f47 72%,#e9eae6 92%)}
.hero-title{position:absolute;right:50px;top:250px;font-family:"Playfair Display",serif;font-style:italic;font-weight:700;font-size:35px;color:var(--purple);line-height:1;white-space:nowrap}
.hero-sub{position:absolute;right:88px;top:287px;font-size:22px;font-weight:300;color:var(--dark);line-height:1;white-space:nowrap}
.dots{position:absolute;left:68px;top:304px;display:flex;gap:6px}
.dots span{width:12px;height:12px;border-radius:50%;background:#b9b9b9;border:1px solid #9d9d9d}
.dots .on{background:#f39a1e;border-color:#e0850c}
.cats{left:58px;top:506px}
.cats h2{font-weight:400;font-size:21px;color:var(--coral);margin-bottom:10px;white-space:nowrap}
.cats li{list-style:none;font-size:9px;color:var(--muted);height:25px;padding-left:4px;white-space:nowrap}
.cats li.active{color:var(--purple)}
.social{left:65px;top:845px;display:flex;gap:7px;font-size:10px;font-weight:500;color:var(--white)}
.social span{display:flex;align-items:center;justify-content:center;height:26px;padding:0 5px}
.social .ch{background:#3f5b98}.social .fl{background:#3fb5e8}
.card{width:162px;height:180px;background:var(--white);border:1px solid var(--line)}
.card .ph{position:absolute;left:10px;top:10px;width:142px;height:116px}
.card .name{position:absolute;left:13px;top:133px;font-size:12px;font-weight:300;color:var(--muted);white-space:nowrap;line-height:14px}
.card .price{position:absolute;left:13px;top:150px;font-size:16px;font-weight:300;color:var(--coral);white-space:nowrap;line-height:18px}
.cta{left:64px;top:934px;width:711px;height:45px;background:var(--coral);border-bottom:3px solid #5b5b5b}
.cta .ph{position:absolute;left:0;top:0;width:101px;height:42px;background:linear-gradient(90deg,#b8a9b8,#efe3d6,#c9b7a5)}
.cta a{position:absolute;left:101px;right:0;top:0;line-height:42px;text-align:center;color:var(--white);font-weight:500;font-size:22px;text-decoration:none;white-space:nowrap}
.cta a svg{vertical-align:middle;margin-left:6px}
.foot-name{left:112px;top:1088px;font-size:16px;font-weight:500;color:var(--dark);white-space:nowrap}
.pay{left:307px;top:1093px;display:flex;gap:4px}
.pay span{height:27px;padding:0 4px;display:flex;align-items:center;background:var(--white);border:1px solid #dcdcdc;font-size:8px;font-weight:500;color:var(--dark);white-space:nowrap}
.copy{left:257px;top:1139px;font-size:9px;font-weight:300;color:var(--muted);white-space:nowrap}
.badge{left:606px;top:1062px;width:90px;height:70px;border-radius:6px;background:linear-gradient(180deg,#e6b766,#f2dfbd)}
</style>
</head>
<body>
<div class="side side--left" role="img" aria-label="Coral side panel with a pattern of pale flowers"></div>
<div class="side side--right" role="img" aria-label="Coral side panel with a pattern of pale flowers"></div>
<main class="page">
  <div class="abs brand">Tom &amp; Nia's</div>
  <nav class="abs nav">
    <a class="home" href="#">Home</a><a class="about" href="#">About Us</a><a class="flowers" href="#">Flowers</a><a class="contact" href="#">Contact Us</a>
  </nav>
  <section class="abs hero">
    <div class="hero-photo" role="img" aria-label="Photo of lily of the valley stems on a green leaf"></div>
    <div class="hero-title">Free delivery</div>
    <div class="hero-sub">with all orders</div>
    <div class="dots"><span class="on"></span><span></span><span></span></div>
  </section>
  <aside class="abs cats">
    <h2>Categories</h2>
    <ul>
      <li class="active">Any Occasion</li><li>Birthday</li><li>Anniversary</li><li>Get Well</li><li>Sympathy and Funeral</li><li>New Baby</li><li>Corporate Gifts</li><li>Love and Romance</li><li>Thank You</li><li>Congratulations</li>
    </ul>
  </aside>
  <div class="abs social"><span class="ch">Chatterly</span><span class="fl">Flitter</span></div>

  <div class="abs card" style="left:221px;top:506px"><div class="ph" role="img" aria-label="Photo of an autumn bouquet wrapped in paper" style="background:linear-gradient(160deg,#e8dccf,#6e5a6b 50%,#8a6b4a)"></div><div class="name">Autumn Love</div><div class="price">Price - £24.99</div></div>
  <div class="abs card" style="left:417px;top:506px"><div class="ph" role="img" aria-label="Photo of a bouquet of red and orange roses" style="background:radial-gradient(circle at 50% 45%,#ef5a3a,#c5231b 60%,#f3efee)"></div><div class="name">Roses are Red</div><div class="price">Price - £49.99</div></div>
  <div class="abs card" style="left:613px;top:506px"><div class="ph" role="img" aria-label="Photo of a lilac and green flower arrangement" style="background:linear-gradient(170deg,#6e6a70,#b7a6c9 45%,#8da36b 80%,#5b5a55)"></div><div class="name">Autumn Wonders</div><div class="price">Price - £27.99</div></div>
  <div class="abs card" style="left:221px;top:708px"><div class="ph" role="img" aria-label="Photo of a pale wedding bouquet with peach roses" style="background:radial-gradient(circle at 55% 55%,#f5c6b0,#eef0e8 50%,#a9a1bd)"></div><div class="name">Wedding Flowers</div><div class="price">Price - £19.99</div></div>
  <div class="abs card" style="left:417px;top:708px"><div class="ph" role="img" aria-label="Photo of a heart shaped flower wreath" style="background:radial-gradient(circle at 50% 50%,#e8e4df 25%,#7f935a 45%,#c98c93 70%,#d9d5cf)"></div><div class="name">Be My Sweetheart</div><div class="price">Price - £35.99</div></div>
  <div class="abs card" style="left:613px;top:708px"><div class="ph" role="img" aria-label="Photo of a bright pink and orange bouquet" style="background:radial-gradient(circle at 50% 45%,#f4b9a3,#e9316a 55%,#e9823b 90%)"></div><div class="name">We are Young, We are Free</div><div class="price">Price - £19.99</div></div>

  <div class="abs cta">
    <div class="ph" role="img" aria-label="Small photo of a pastel bouquet"></div>
    <a href="#">Order today: 0203 574 2261 or Email us<svg width="8" height="10" viewBox="0 0 8 10"><path d="M0 0L8 5L0 10Z" fill="#fff"/></svg></a>
  </div>

  <div class="abs foot-name">Tom &amp; Nia's</div>
  <div class="abs pay"><span>KORVA</span><span>Paymoriant</span><span>Harbour Quickcard</span><span>Zentrip</span></div>
  <div class="abs copy">Copyright © Tom&amp;Nia's. &nbsp;All Rights Reserved. &nbsp;| &nbsp;Privacy Policy &nbsp;| &nbsp;Terms of Use</div>
  <div class="abs badge" role="img" aria-label="The Northfield Petal Guild membership badge"></div>
</main>
</body>
</html>
```